Cobalt Ridge Mini Storage - Ad for half Page

Need half page ad for a publication.
would also like to be able to use in the future
self storage facility - 3 locations, the third opening soon
do not like real busy projects...i have a logo but willing to tweak if needed

```html
<!DOCTYPE html>
<html lang="en">
<head>
<meta charset="utf-8">
<title>Cobalt Ridge Mini Storage – Half Page Ad</title>
<link rel="stylesheet" href="https://fonts.googleapis.com/css2?family=Montserrat:wght@800&family=Hind:wght@400;500;600&family=Roboto:wght@700&family=Arimo:wght@400&display=swap">
<style>
  :root {
    --page-bg: #efefef;
    --paper: #ffffff;
    --brown-dark: #5b2f12;
    --brown-mid: #7a4511;
    --brown-warm: #a0621c;
    --tan: #e8c28d;
    --cream: #faf3e6;
    --label: #b8741f;
    --icon: #4d4d4d;
    --ink: #333333;
    --white: #ffffff;
  }
  * { box-sizing: border-box; margin: 0; padding: 0; }
  html, body { width: 800px; height: 1200px; overflow: hidden; background: var(--page-bg); }
  .ad {
    position: absolute; left: 20px; top: 372px; width: 760px; height: 456px;
    background: var(--paper); box-shadow: 0 4px 10px rgba(0,0,0,.25); overflow: hidden;
  }
  .hero-photo {
    position: absolute; left: 0; top: 0; width: 760px; height: 226px;
    background:
      linear-gradient(90deg, var(--brown-dark) 0%, rgba(91,47,18,.85) 25%, rgba(91,47,18,.35) 55%, rgba(91,47,18,.1) 100%),
      linear-gradient(180deg, #9a9a5a 0%, #b9aa94 12%, #a89f98 40%, #b59c7c 60%, #c7ab8a 100%);
  }
  .headline {
    position: absolute; left: 19px; top: 20px;
    font-family: "Montserrat", sans-serif; font-weight: 800; font-size: 40px;
    line-height: 34px; letter-spacing: -0.5px; text-transform: uppercase; color: var(--white);
  }
  .headline .accent { color: var(--tan); display: block; }
  .intro {
    position: absolute; left: 19px; top: 174px; width: 250px;
    font-family: "Roboto", sans-serif; font-weight: 700; font-size: 8.6px; line-height: 12px; color: var(--white);
  }
  .location-box {
    position: absolute; left: 622px; width: 123px; height: 102px;
    background: linear-gradient(180deg, var(--brown-warm) 0%, #6c3713 100%);
    color: var(--white); text-align: center; font-family: "Hind", sans-serif;
    display: flex; flex-direction: column; align-items: center; justify-content: center;
  }
  .location-box .pin { width: 10px; height: 14px; margin-bottom: 3px; }
  .location-box .city { font-size: 14px; font-weight: 500; line-height: 14px; color: #f6dcb2; text-transform: uppercase; }
  .location-box .address { font-family: "Arimo", sans-serif; font-size: 8.5px; line-height: 10px; margin-top: 3px; }
  .location-box.soon .city { font-size: 18px; line-height: 20px; }
  .box-1 { top: 36px; } .box-2 { top: 154px; } .box-3 { top: 272px; }
  .options-title {
    position: absolute; left: 91px; top: 233px; width: 434px; height: 33px; border-radius: 17px;
    background: linear-gradient(180deg, #6a3a0c 0%, var(--brown-warm) 55%, #6a3a0c 100%);
    box-shadow: 0 2px 3px rgba(0,0,0,.3);
    font-family: "Hind", sans-serif; font-weight: 400; font-size: 18px; line-height: 35px;
    text-align: center; color: var(--tan); text-transform: uppercase;
  }
  .options {
    position: absolute; left: 39px; top: 272px; width: 542px; height: 108px;
    background: var(--cream); display: flex; padding: 8px 0;
  }
  .option {
    flex: 1; display: flex; flex-direction: column; align-items: center;
    border-right: 1px solid #555; padding-top: 2px;
  }
  .option:last-child { border-right: none; }
  .option svg { width: 44px; height: 42px; margin-bottom: 6px; }
  .option .label {
    font-family: "Hind", sans-serif; font-weight: 600; font-size: 12.5px; line-height: 13px;
    text-align: center; color: var(--label); text-transform: uppercase;
  }
  .brand { position: absolute; left: 18px; top: 389px; display: flex; align-items: center; gap: 10px; }
  .brand .mark { width: 48px; height: 48px; background: var(--brown-warm); }
  .brand .name {
    font-family: "Montserrat", sans-serif; font-weight: 800; font-size: 19px; line-height: 22px; color: var(--brown-dark);
  }
  .contact { position: absolute; font-family: "Arimo", sans-serif; color: var(--ink); font-size: 11px; line-height: 16px; }
  .contact .region { font-family: "Hind", sans-serif; font-weight: 500; font-size: 9px; color: var(--label); text-transform: uppercase; margin-bottom: 2px; }
  .contact .line { display: flex; align-items: center; gap: 8px; }
  .contact svg { width: 10px; height: 10px; }
  .contact-1 { left: 317px; top: 391px; }
  .contact-2 { left: 554px; top: 393px; }
  .divider { position: absolute; left: 529px; top: 410px; width: 2px; height: 18px; background: var(--label); }
</style>
</head>
<body>
<main class="ad">
  <div class="hero-photo" role="img" aria-label="Aerial photo of the storage facility with parked cars in front"></div>

  <h1 class="headline">Friendly,<br>Convenient<span class="accent">Storage<br>Solutions!</span></h1>
  <p class="intro">At Cobalt Ridge Mini Storage, We're Here To Help You Store Your Possessions In Clean, Secure Lockers With 24/7 Gated Access.</p>

  <section class="location-box box-1">
    <svg class="pin" viewBox="0 0 10 14"><path d="M5 0a5 5 0 0 0-5 5c0 3.5 5 9 5 9s5-5.5 5-9a5 5 0 0 0-5-5zm0 7a2 2 0 1 1 0-4 2 2 0 0 1 0 4z" fill="#f6dcb2"/></svg>
    <div class="city">Harlan Springs</div>
    <div class="address">4820 Lakeview Parkway<br>Harlan Springs,<br>TX 78001</div>
  </section>
  <section class="location-box box-2">
    <svg class="pin" viewBox="0 0 10 14"><path d="M5 0a5 5 0 0 0-5 5c0 3.5 5 9 5 9s5-5.5 5-9a5 5 0 0 0-5-5zm0 7a2 2 0 1 1 0-4 2 2 0 0 1 0 4z" fill="#f6dcb2"/></svg>
    <div class="city">Westbrook</div>
    <div class="address">316 Mill Street Suite<br>110 Westbrook,<br>TX 78002</div>
  </section>
  <section class="location-box box-3 soon">
    <svg class="pin" viewBox="0 0 10 14"><path d="M5 0a5 5 0 0 0-5 5c0 3.5 5 9 5 9s5-5.5 5-9a5 5 0 0 0-5-5zm0 7a2 2 0 1 1 0-4 2 2 0 0 1 0 4z" fill="#f6dcb2"/></svg>
    <div class="city">Opening<br>Soon!</div>
  </section>

  <h2 class="options-title">Our Storage Options</h2>
  <section class="options">
    <div class="option">
      <svg viewBox="0 0 44 42"><path d="M10 22a7 7 0 0 1 3-13 10 10 0 0 1 19 2 6 6 0 0 1 1 11z" fill="var(--icon)"/><path d="M12 27l-2 4M18 26l-3 6 3-1-2 5M26 26l-2 4M32 27l-3 6 3-1-2 5M22 32l-2 4" stroke="var(--icon)" stroke-width="1.6" fill="none"/></svg>
      <div class="label">Climate<br>Controlled<br>Units</div>
    </div>
    <div class="option">
      <svg viewBox="0 0 44 42"><path d="M2 14L22 3l20 11v2H2z" fill="var(--icon)"/><rect x="5" y="17" width="34" height="23" fill="none" stroke="var(--icon)" stroke-width="2.5"/><g fill="var(--icon)"><rect x="9" y="21" width="7" height="5"/><rect x="18" y="21" width="7" height="5"/><rect x="27" y="21" width="8" height="5"/><rect x="9" y="28" width="7" height="5"/><rect x="18" y="28" width="7" height="5"/><rect x="27" y="28" width="8" height="5"/><rect x="9" y="34" width="26" height="4"/></g></svg>
      <div class="label">Non-Climate<br>Controlled<br>Units</div>
    </div>
    <div class="option">
      <svg viewBox="0 0 44 42"><path d="M22 2v30H8z" fill="var(--icon)"/><path d="M24 10l10 22H24z" fill="var(--icon)"/><path d="M4 34h36l-5 6H9z" fill="var(--icon)"/></svg>
      <div class="label">Boat and RV<br>Storage</div>
    </div>
    <div class="option">
      <svg viewBox="0 0 44 42"><rect x="12" y="3" width="20" height="37" fill="none" stroke="var(--icon)" stroke-width="2.5"/><rect x="4" y="16" width="8" height="24" fill="none" stroke="var(--icon)" stroke-width="2.5"/><rect x="32" y="16" width="8" height="24" fill="none" stroke="var(--icon)" stroke-width="2.5"/><g fill="var(--icon)"><rect x="16" y="8" width="4" height="4"/><rect x="24" y="8" width="4" height="4"/><rect x="16" y="15" width="4" height="4"/><rect x="24" y="15" width="4" height="4"/><rect x="16" y="22" width="4" height="4"/><rect x="24" y="22" width="4" height="4"/><rect x="19" y="31" width="6" height="9"/></g></svg>
      <div class="label">Office and<br>Wirehouse<br>Space</div>
    </div>
  </section>

  <div class="brand">
    <div class="mark"></div>
    <div class="name">Cobalt Ridge<br>Mini Storage</div>
  </div>

  <div class="contact contact-1">
    <div class="region">Harlan Springs</div>
    <div class="line"><svg viewBox="0 0 10 10"><path d="M2 0l2 2-1 2c1 1 2 2 3 3l2-1 2 2-2 2C4 9 1 6 0 2z" fill="var(--label)"/></svg>(555) 014-3700</div>
    <div class="line"><svg viewBox="0 0 10 10"><circle cx="5" cy="5" r="4.3" fill="none" stroke="var(--label)" stroke-width="1.2"/><path d="M1 5h8M5 1c-2 2-2 6 0 8M5 1c2 2 2 6 0 8" stroke="var(--label)" stroke-width="0.9" fill="none"/></svg>sales@cobaltridgestorage.com</div>
  </div>
  <div class="divider"></div>
  <div class="contact contact-2">
    <div class="region">Westbrook</div>
    <div class="line"><svg viewBox="0 0 10 10"><path d="M2 0l2 2-1 2c1 1 2 2 3 3l2-1 2 2-2 2C4 9 1 6 0 2z" fill="var(--label)"/></svg>(555) 018-7741</div>
    <div class="line"><svg viewBox="0 0 10 10"><circle cx="5" cy="5" r="4.3" fill="none" stroke="var(--label)" stroke-width="1.2"/><path d="M1 5h8M5 1c-2 2-2 6 0 8M5 1c2 2 2 6 0 8" stroke="var(--label)" stroke-width="0.9" fill="none"/></svg>sales@cobaltridgestorage.com</div>
  </div>
</main>
</body>
</html>
```